Business Card Design

We need a business card designed which uses our logo and looks really good. The company is called LumaPivot482. We help e-commerce companies reduce cart abandonment by rescuing the sale through our innovative technology.

Our corporate colors are red, black and white.

I have attached our AI file for the logo as well.
Updates

Additional information for the business card:

Name: Derek Malloy
Title: President/CTO
Phone: 1-855-LUMA-482
Website: www.lumapivot482.com
Email: derek@lumapivot482.com

Tag line: Turning Browsers Into Orders

Industry/Entity Type

E-Commerce

```html
<!DOCTYPE html>
<html lang="en">
<head>
<meta charset="utf-8">
<title>LumaPivot482 — Business Card</title>
<link rel="stylesheet" href="https://fonts.googleapis.com/css2?family=Mulish:wght@400;500;700&display=swap">
<style>
  :root {
    --backdrop: #e4e2df;
    --card: #5b5b5c;
    --ink-white: #f4f4f4;
    --ink-grey: #a9a9aa;
    --ink-black: #1c1c1c;
    --accent-red: #d7141a;
    --rule: #c9c9c9;
  }
  * { margin: 0; padding: 0; box-sizing: border-box; }
  html, body {
    width: 1200px; height: 780px; overflow: hidden;
    background: var(--backdrop);
    font-family: "Mulish", "Helvetica Neue", Arial, sans-serif;
  }
  .stage {
    width: 1200px; height: 780px;
    display: flex; align-items: center; justify-content: center;
  }
  .card {
    position: relative;
    width: 1000px; height: 572px;
    background: var(--card);
    border-radius: 4px;
    box-shadow: 0 10px 30px rgba(0,0,0,0.18);
    overflow: hidden;
  }
  .rule-left {
    position: absolute; left: 0; top: 188px;
    width: 488px; height: 1px; background: var(--rule);
  }
  .rule-right {
    position: absolute; left: 902px; top: 112px;
    width: 98px; height: 1px; background: var(--rule);
  }
  .rule-dashed {
    position: absolute; left: 900px; top: 0; bottom: 0; width: 2px;
  }
  .identity {
    position: absolute; right: 130px; top: 112px;
    text-align: right;
  }
  .tagline {
    color: var(--ink-grey);
    font-size: 17px; font-weight: 500;
    letter-spacing: 0.22em; text-transform: uppercase;
    margin-bottom: 6px;
  }
  .brand {
    display: flex; align-items: center; justify-content: flex-end; gap: 12px;
  }
  .brand-mark {
    width: 22px; height: 22px; background: var(--accent-red);
  }
  .brand-name {
    color: var(--ink-black);
    font-size: 48px; font-weight: 500; line-height: 1;
    letter-spacing: 0.02em;
  }
  .person { margin-top: 30px; color: var(--ink-white); }
  .person-name { font-size: 30px; font-weight: 700; line-height: 1.2; }
  .person-title { font-size: 29px; font-weight: 400; line-height: 1.25; }
  .contact {
    margin-top: 26px; color: var(--ink-white);
    font-size: 26px; font-weight: 400; line-height: 1.3;
    list-style: none;
  }
  .contact .phone { margin-bottom: 14px; }
</style>
</head>
<body>
  <main class="stage">
    <section class="card" aria-label="LumaPivot482 business card">
      <div class="rule-left"></div>
      <div class="rule-right"></div>
      <svg class="rule-dashed" viewBox="0 0 2 572" preserveAspectRatio="none" aria-hidden="true">
        <line x1="1" y1="0" x2="1" y2="572" stroke="#d5d5d5" stroke-width="2" stroke-dasharray="12 9"/>
      </svg>

      <div class="identity">
        <p class="tagline">Turning Browsers Into Orders</p>
        <div class="brand">
          <span class="brand-mark" aria-hidden="true"></span>
          <span class="brand-name">LumaPivot482</span>
        </div>

        <div class="person">
          <p class="person-name">Derek Malloy</p>
          <p class="person-title">President / CTO</p>
        </div>

        <ul class="contact">
          <li class="phone">1-855-LUMA-482</li>
          <li class="email">derek@lumapivot482.com</li>
          <li class="web">www.lumapivot482.com</li>
        </ul>
      </div>
    </section>
  </main>
</body>
</html>
```